Awesome photographers card for an awesome new business

Double sided business card Black background and silver logo in middle on one side. Details on otherside. please keep it simple

Photographer

Gavin Tolley
0482615073
GavinTolleyPhotography82@lumenpost.com
www.GavinTolleyPhotography.com.au
Instagram _Gavin_tolley

Requirements
Must have
• My logo in Silver
• please use instagram logo instead of "Instagram"

```html
<!DOCTYPE html>
<html lang="en">
<head>
<meta charset="utf-8">
<title>Gavin Tolley Photography – Business Card</title>
<link rel="stylesheet" href="https://fonts.googleapis.com/css2?family=Open+Sans:wght@400;600&display=swap">
<style>
  :root {
    --stage: #0c0c0d;
    --card-dark: #1c1b1b;
    --card-dark-pattern: #2a2929;
    --silver: #e4e4e4;
    --silver-dim: #bdbdbd;
    --card-light: #f6f6f6;
    --card-light-pattern: #e6e6e6;
    --ink: #1e1e1e;
    --ink-soft: #4a4a4a;
    --rule: #9a9a9a;
    --bracket-gold: #8a7b6c;
  }
  * { box-sizing: border-box; margin: 0; padding: 0; }
  html, body { width: 1200px; height: 1200px; overflow: hidden; }
  body {
    background: var(--stage);
    font-family: "Open Sans", Arial, sans-serif;
    position: relative;
  }
  .card {
    position: absolute;
    width: 760px;
    height: 434px;
    border-radius: 4px;
    overflow: hidden;
    box-shadow: 0 24px 50px rgba(0,0,0,.6);
  }
  .card__pattern {
    position: absolute; inset: 0;
  }
  .card__brackets { position: absolute; inset: 0; }

  /* Front */
  .card--front { left: 70px; top: 120px; background: var(--card-dark); }
  .card--front .card__pattern {
    background: radial-gradient(ellipse at 75% 20%, var(--card-dark-pattern), transparent 55%),
                radial-gradient(ellipse at 20% 80%, var(--card-dark-pattern), transparent 55%);
  }
  .brand {
    position: absolute; left: 50%; top: 50%;
    transform: translate(-50%, -50%);
    display: flex; flex-direction: column; align-items: center; gap: 14px;
  }
  .brand__ring {
    width: 150px; height: 150px; border-radius: 50%;
    border: 4px solid var(--silver);
  }
  .brand__name {
    color: var(--silver);
    font-weight: 600;
    font-size: 26px;
    letter-spacing: 6px;
    text-transform: uppercase;
  }

  /* Back */
  .card--back { left: 370px; top: 640px; background: var(--card-light); }
  .card--back .card__pattern {
    background: radial-gradient(ellipse at 80% 15%, var(--card-light-pattern), transparent 55%),
                radial-gradient(ellipse at 15% 65%, var(--card-light-pattern), transparent 50%);
  }
  .details {
    position: absolute; left: 0; right: 0; top: 62px;
    display: flex; flex-direction: column; align-items: center;
    color: var(--ink);
  }
  .details__name {
    font-size: 40px; font-weight: 400; letter-spacing: 1px;
    text-transform: uppercase;
  }
  .details__rule {
    width: 330px; height: 1px; background: var(--rule); margin: 12px 0;
  }
  .contact {
    display: flex; align-items: center; gap: 10px;
    font-size: 22px; color: var(--ink-soft); line-height: 1.55;
  }
  .contact--lg { font-size: 21px; color: var(--ink); }
  .contact svg { width: 20px; height: 20px; flex: none; }
  .social-dot {
    width: 18px; height: 18px; border-radius: 50%;
    background: var(--ink-soft); flex: none;
  }
  .details__spacer { height: 30px; }
</style>
</head>
<body>

  <section class="card card--front" aria-label="Business card front">
    <div class="card__pattern" role="img" aria-label="Faint dark floral pattern background"></div>
    <svg class="card__brackets" viewBox="0 0 760 434" fill="none" stroke="#d0d0d0" stroke-width="2">
      <path d="M600 40 H650 V90"/>
      <path d="M110 344 V394 H160"/>
      <path d="M110 140 V100 H150" opacity="0"/>
    </svg>
    <div class="brand">
      <div class="brand__ring"></div>
      <div class="brand__name">Gavin Tolley</div>
    </div>
  </section>

  <section class="card card--back" aria-label="Business card back">
    <div class="card__pattern" role="img" aria-label="Faint light floral pattern background"></div>
    <svg class="card__brackets" viewBox="0 0 760 434" fill="none" stroke="var(--bracket-gold)" stroke-width="2">
      <path d="M40 110 V70 H80"/>
      <path d="M680 40 H720 V80"/>
      <path d="M40 330 V370 H80"/>
      <path d="M720 310 V350 H680"/>
    </svg>
    <div class="details">
      <h1 class="details__name">Gavin Tolley</h1>
      <div class="details__rule"></div>
      <p class="contact">
        <svg viewBox="0 0 24 24" fill="var(--ink-soft)"><path d="M6.6 10.8a15.2 15.2 0 0 0 6.6 6.6l2.2-2.2a1 1 0 0 1 1-.25 11.4 11.4 0 0 0 3.6.6 1 1 0 0 1 1 1V20a1 1 0 0 1-1 1A17 17 0 0 1 3 4a1 1 0 0 1 1-1h3.5a1 1 0 0 1 1 1c0 1.25.2 2.45.6 3.6a1 1 0 0 1-.25 1z"/></svg>
        0482615073
      </p>
      <p class="contact"><span class="social-dot"></span>_Gavin_tolley</p>
      <div class="details__rule"></div>
      <div class="details__spacer"></div>
      <p class="contact contact--lg">
        <svg viewBox="0 0 24 24" fill="none" stroke="var(--ink)" stroke-width="1.6"><circle cx="12" cy="12" r="9"/><ellipse cx="12" cy="12" rx="4" ry="9"/><path d="M3 12h18M5 7h14M5 17h14"/></svg>
        www.GavinTolleyPhotography.com.au
      </p>
      <p class="contact contact--lg">
        <svg viewBox="0 0 24 24" fill="none" stroke="var(--ink)" stroke-width="1.6"><rect x="3" y="5" width="18" height="14" rx="1"/><path d="M3 6l9 7 9-7"/></svg>
        GavinTolleyPhotography82@lumenpost.com
      </p>
    </div>
  </section>

</body>
</html>
```